Advanced Therapeutic Massage Therapist

I need a business card advertising my massage services as an advanced therapeutic massage therapist. I offer advanced therapeutic massage, swedish and deep tissue. I want to create a simple, professional and feminine card. I like bright colours and creativity.

I prefer a bold and experimental approach rather than something status-quo. A card to suggest therapeutic healing through dynamic massage. Motifs, shapes or layout which suggest movement and flow.

Target Market(s)

Everybody!

Industry/Entity Type

Health And Wellness

Contact Information for Business Card

The card should include:
My name, logo, services offered and my contact details.

Siobhán Delaney
Massage Therapist

- Swedish - Deep Tissue - Advanced Therapeutic

Phone: (+353) 87 296 1740
Email: regenerate@siobhandelaney-example.com
Website: www.siobhandelany-example.com

Font styles to use
Serif
Sans Serif
Decorative
Script

Colors

Designer to choose colors to be used in the design.

Requirements
Must have
• An example may contain something like this, yet concise:
• "Siobhán Delaney
• Massage Therapist
• - Swedish - Deep Tissue - Advanced Therapeutic"
Nice to have
• This sentence is optional:
• Imagery such as a logo or symbol. I have attached a file containing a logo I had produced however the name is incorrect now as it is "Siobhán" not "Sadie". It could be edited to change it to Siobhán.
• I have sent the file as .psd .jpg. .pdf and .png
• I like when the card conveys energy, movement, pressure points, flow etc.
• I just like the designer to follow their own style and ideas. I like bright colours but must have a lot of a base colour to offset it. I really prefer them to follow their own inspiration. That is my preference.
Should not have
• Pine trees, non-native trees to Britain and Ireland, exotic flowers or animals that are not native to Britain and Ireland.
• I don't like brown as the background colour of the card.
• The cars shouldn't look like a wedding invitation i.e too many floral type designs.

```html
<!DOCTYPE html>
<html lang="en">
<head>
<meta charset="utf-8">
<title>Siobhán Delaney – Massage Therapist Business Card</title>
<link rel="stylesheet" href="https://fonts.googleapis.com/css2?family=Great+Vibes&family=Open+Sans:wght@400;600&display=swap">
<style>
  :root {
    --stage: #e9e6e2;
    --card-light-top: #ffffff;
    --card-light-bottom: #dcdcdc;
    --card-dark-top: #262626;
    --card-dark-bottom: #161616;
    --ink: #1e1e1e;
    --ink-soft: #3a3a3a;
    --paper: #ffffff;
    --paper-soft: #d9d9d9;
    --mark-light: #9a9a9a;
    --mark-dark: #bdbdbd;
    --mark-ghost: rgba(255, 255, 255, 0.035);
  }
  * { box-sizing: border-box; margin: 0; padding: 0; }
  html, body {
    width: 1200px;
    height: 775px;
    overflow: hidden;
    background: var(--stage);
  }
  .canvas {
    position: relative;
    width: 1200px;
    height: 775px;
  }
  .card {
    position: absolute;
    top: 214px;
    width: 530px;
    height: 347px;
    border-radius: 22px;
    overflow: hidden;
    box-shadow: 0 6px 16px rgba(0, 0, 0, 0.25);
  }
  .card--front {
    left: 50px;
    background: linear-gradient(160deg, var(--card-light-top) 20%, var(--card-light-bottom) 100%);
    color: var(--ink);
  }
  .card--back {
    left: 620px;
    background: linear-gradient(160deg, var(--card-dark-top) 0%, var(--card-dark-bottom) 100%);
    color: var(--paper);
  }
  .emblem {
    position: absolute;
    border-radius: 50%;
  }
  .card--front .emblem {
    left: 347px;
    top: 14px;
    width: 160px;
    height: 160px;
    background: radial-gradient(circle, #cfcfcf 0%, var(--mark-light) 100%);
  }
  .card--back .emblem {
    left: 268px;
    top: 44px;
    width: 168px;
    height: 168px;
    background: radial-gradient(circle, #8a8a8a 0%, var(--mark-dark) 100%);
  }
  .card--back .emblem-ghost {
    position: absolute;
    left: -110px;
    top: -10px;
    width: 330px;
    height: 360px;
    border-radius: 50%;
    background: var(--mark-ghost);
  }
  .name {
    font-family: "Great Vibes", cursive;
    font-weight: 400;
    line-height: 1;
    position: absolute;
    white-space: nowrap;
  }
  .role {
    font-family: "Open Sans", sans-serif;
    position: absolute;
    line-height: 1;
    white-space: nowrap;
  }
  .card--front .name {
    left: 29px;
    top: 206px;
    font-size: 34px;
    color: var(--ink);
  }
  .card--front .role {
    left: 30px;
    top: 242px;
    font-size: 12.5px;
    color: var(--ink-soft);
  }
  .rule {
    position: absolute;
    left: 29px;
    top: 265px;
    width: 470px;
    height: 3px;
    background: var(--ink);
  }
  .contact {
    position: absolute;
    left: 42px;
    top: 281px;
    display: flex;
    align-items: center;
    white-space: nowrap;
    font-family: "Open Sans", sans-serif;
    font-size: 16px;
    line-height: 1.2;
    color: var(--ink);
  }
  .contact__item { display: flex; align-items: center; gap: 9px; white-space: nowrap; flex: none; }
  .contact__divider { margin: 0 20px 0 26px; flex: none; }
  .icon { width: 22px; height: 18px; fill: var(--ink); flex: none; }
  .card--back .name {
    left: 0;
    width: 100%;
    text-align: center;
    top: 218px;
    font-size: 34px;
    padding-left: 12px;
  }
  .card--back .role {
    left: 0;
    width: 100%;
    text-align: center;
    padding-left: 12px;
    top: 254px;
    font-size: 12.5px;
    color: var(--paper-soft);
  }
  .services {
    position: absolute;
    left: 0;
    width: 100%;
    text-align: center;
    padding-left: 12px;
    top: 279px;
    white-space: nowrap;
    font-family: "Open Sans", sans-serif;
    font-size: 14.5px;
    color: var(--paper);
  }
</style>
</head>
<body>
<main class="canvas">
  <section class="card card--front">
    <div class="emblem" role="img" aria-label="Circular tree of life emblem"></div>
    <h1 class="name">Siobhán Delaney</h1>
    <p class="role">Massage Therapist</p>
    <div class="rule"></div>
    <div class="contact">
      <span class="contact__item">
        <svg class="icon" viewBox="0 0 24 20" aria-hidden="true">
          <path d="M2 6c0-3 4-4 10-4s10 1 10 4v2h-5V6.5c-1.5-.6-3-.8-5-.8s-3.5.2-5 .8V8H2z"/>
          <path d="M5 9h14l2 9H3z"/>
          <circle cx="12" cy="13.5" r="2.6" fill="#fff"/>
        </svg>
        (+353) 87 296 1740
      </span>
      <span class="contact__divider">I</span>
      <span class="contact__item">
        <svg class="icon" viewBox="0 0 24 18" aria-hidden="true">
          <path d="M1 2h22v14H1z"/>
          <path d="M2 3l10 8 10-8" fill="none" stroke="#fff" stroke-width="1.8"/>
        </svg>
        siobhanmassage@example.ie
      </span>
    </div>
  </section>

  <section class="card card--back">
    <div class="emblem-ghost" role="img" aria-label="Faint large tree of life emblem decoration"></div>
    <div class="emblem" role="img" aria-label="Circular tree of life emblem"></div>
    <h2 class="name">Siobhán Delaney</h2>
    <p class="role">Massage Therapist</p>
    <p class="services">Swedish - Deep Tissue - Advanced Therapeutic</p>
  </section>
</main>
</body>
</html>
```